KL Taxidermy

I need business Cards with my logo and a background photo of one of my taxidermy mounts.
I would like a black back drop behind it all and what ever looks best for my contact information (red or white?)
Garrick Pembley
592-718-4409
kltaxidermy482@mailnook.example
Chatterloom page

```html
<!DOCTYPE html>
<html lang="en">
<head>
<meta charset="utf-8">
<title>KL Taxidermy Business Card</title>
<link rel="stylesheet" href="https://fonts.googleapis.com/css2?family=Montserrat:wght@500;600&family=Open+Sans:wght@400&display=swap">
<style>
  :root {
    --stage: #2a2a2a;
    --card: #1d1d1d;
    --red: #e61e25;
    --white: #ffffff;
    --antler-light: #d8ccba;
    --antler-dark: #8d7a64;
  }
  * { margin: 0; padding: 0; box-sizing: border-box; }
  html, body { width: 1200px; height: 895px; overflow: hidden; background: var(--stage); }
  .stage {
    width: 1200px; height: 895px;
    display: flex; flex-direction: column; align-items: center; justify-content: center; gap: 28px;
  }
  .card {
    position: relative;
    width: 720px; height: 412px;
    background: var(--card);
    overflow: hidden;
  }
  .mount-photo {
    position: absolute; left: 190px; top: 90px; width: 340px; height: 190px;
    border-radius: 40%;
    background: radial-gradient(ellipse at center, var(--antler-light) 0%, var(--antler-dark) 60%, rgba(29,29,29,0) 72%);
  }
  .brand {
    position: absolute; left: 90px; top: 218px;
    display: flex; align-items: center; gap: 12px;
    font-family: "Montserrat", sans-serif; font-weight: 600; font-size: 22px;
    letter-spacing: 2px; text-transform: uppercase; color: var(--white);
  }
  .brand-dot { width: 14px; height: 14px; border-radius: 50%; background: var(--white); }
  .contact { position: absolute; left: 372px; top: 96px; }
  .contact-name {
    font-family: "Montserrat", sans-serif; font-weight: 500; font-size: 30px;
    color: var(--red); text-transform: uppercase; letter-spacing: 0.5px; line-height: 1;
  }
  .contact-list { list-style: none; margin: 10px 0 0 14px; position: relative; }
  .contact-list::before {
    content: ""; position: absolute; left: 13px; top: -8px; bottom: 18px;
    width: 1px; background: var(--white);
  }
  .contact-item {
    display: flex; align-items: center; gap: 12px; margin-bottom: 8px;
    font-family: "Open Sans", sans-serif; font-size: 16px; color: var(--white);
  }
  .contact-icon { width: 28px; height: 28px; flex: none; position: relative; }
  .bottom-band {
    position: absolute; left: 0; right: 0; bottom: 8px; height: 14px; background: var(--red);
  }
  .band-mark { position: absolute; left: 560px; bottom: 4px; width: 22px; height: 22px; }
</style>
</head>
<body>
<main class="stage">
  <section class="card card-front">
    <div class="mount-photo" role="img" aria-label="Photo of a moose antler and skull taxidermy mount"></div>
  </section>

  <section class="card card-back">
    <div class="brand"><span class="brand-dot"></span>KL Taxidermy</div>

    <div class="contact">
      <h1 class="contact-name">Garrick Pembley</h1>
      <ul class="contact-list">
        <li class="contact-item">
          <svg class="contact-icon" viewBox="0 0 28 28" aria-hidden="true">
            <polygon points="14,2 25,8 25,20 14,26 3,20 3,8" fill="#e61e25"/>
            <path d="M9 11c1 4 4 7 8 8l2-2-2-2-2 1c-1-1-2-2-3-3l1-2-2-2z" fill="#fff"/>
          </svg>
          592-718-4409
        </li>
        <li class="contact-item">
          <svg class="contact-icon" viewBox="0 0 28 28" aria-hidden="true">
            <polygon points="14,2 25,8 25,20 14,26 3,20 3,8" fill="#e61e25"/>
            <rect x="8" y="10" width="12" height="9" fill="none" stroke="#fff" stroke-width="1.5"/>
            <path d="M8 10l6 5 6-5" fill="none" stroke="#fff" stroke-width="1.5"/>
          </svg>
          kltaxidermy482@mailnook.example
        </li>
      </ul>
    </div>

    <div class="bottom-band"></div>
    <svg class="band-mark" viewBox="0 0 22 22" aria-hidden="true">
      <polygon points="11,1 14,8 21,11 14,14 11,21 8,14 1,11 8,8" fill="#ffffff"/>
    </svg>
  </section>
</main>
</body>
</html>
```